I need to redesign this website. Modern Fun Professional Redesign For www.GladPerksHub.com = New Name www.ClaimVouchly.com

Use existing content as it is on website exactly and we will revise after initial mock ups.

The new name will be ClaimVouchly.com please make a quick logo for this site too while redesigning.

Make it look like an official website....

Target Market(s)

Consumers that are redeeming certificates that businesses gave to them as a gift for customer loyalty,e tc.

Industry/Entity Type

It Professional

Logo Text

www.ClaimVouchly.com

Number of Pages Required

4 page

Colors

Designer to choose colors to be used in the design.

Requirements
Must have
• Must look professional, build trust and credibility.
Nice to have
• open
Should not have
• open

```html
<!DOCTYPE html>
<html lang="en">
<head>
<meta charset="utf-8">
<title>ClaimVouchly.com – Redemption Source</title>
<link href="https://fonts.googleapis.com/css2?family=Questrial&family=Lexend:wght@400;500;600;700&display=swap" rel="stylesheet">
<style>
  :root {
    --page-bg: #e5e3e3;
    --header-bg: #e4e2e2;
    --ink: #111111;
    --ink-soft: #2b2b2b;
    --muted: #777777;
    --accent: #ff0000;
    --white: #ffffff;
    --footer-bg: #252525;
    --field-bg: #a9a9a9;
    --hero-light: #f3f3f3;
    --hero-mid: #dcdcdc;
    --testi-dark: #3c3c3c;
    --testi-mid: #6b6b6b;
  }
  * { box-sizing: border-box; margin: 0; padding: 0; }
  html, body { width: 1200px; height: 2400px; overflow: hidden; }
  body {
    position: relative;
    background: var(--page-bg);
    font-family: "Questrial", "Lexend", sans-serif;
    color: var(--ink);
  }
  .abs { position: absolute; }
  .center-x { left: 0; width: 1200px; text-align: center; white-space: nowrap; }

  /* Header */
  .site-header { position: absolute; left: 0; top: 0; width: 1200px; height: 134px; background: var(--header-bg); }
  .brand { left: 32px; top: 40px; font-size: 40px; color: var(--ink); white-space: nowrap; }
  .main-nav { right: 36px; top: 50px; display: flex; gap: 18px; font-size: 23px; }
  .main-nav a { color: var(--muted); text-decoration: none; position: relative; }
  .main-nav a.active { color: var(--accent); }
  .main-nav a.active::after { content: ""; position: absolute; left: 0; right: 0; bottom: -16px; height: 2px; background: var(--ink-soft); }

  /* Hero */
  .hero-photo { position: absolute; left: 0; top: 134px; width: 1200px; height: 778px; }
  .hero-title { top: 394px; font-family: "Lexend", sans-serif; font-weight: 500; font-size: 39px; color: var(--ink); }
  .hero-sub { top: 446px; font-size: 22px; color: var(--ink); }
  .hero-note { top: 486px; font-family: "Lexend", sans-serif; font-weight: 500; font-size: 18px; color: var(--muted); }
  .redeem-form { left: 266px; top: 532px; width: 656px; height: 68px; }
  .redeem-input { position: absolute; left: 0; top: 0; width: 504px; height: 68px; background: var(--white); border-radius: 10px 0 0 10px; padding-left: 26px; line-height: 68px; font-size: 15px; color: var(--ink-soft); }
  .redeem-btn { position: absolute; left: 492px; top: 0; width: 164px; height: 68px; background: var(--accent); border-radius: 10px; color: var(--white); font-size: 38px; text-align: center; line-height: 68px; }

  /* About */
  .about-line { font-size: 15px; color: var(--ink); text-transform: uppercase; }

  /* Testimonial */
  .testimonial-photo { position: absolute; left: 40px; top: 1208px; width: 1124px; height: 620px; }
  .testi-title { top: 1248px; font-family: "Lexend", sans-serif; font-weight: 500; font-size: 42px; color: var(--white); }
  .testi-rule { left: 460px; top: 1306px; width: 68px; height: 6px; background: var(--accent); }
  .testi-name { top: 1452px; font-family: "Lexend", sans-serif; font-weight: 600; font-size: 26px; color: var(--white); }
  .testi-meta { font-family: "Lexend", sans-serif; font-weight: 600; font-size: 11px; color: var(--white); }
  .testi-quote { left: 40px; width: 1124px; top: 1536px; text-align: center; white-space: nowrap; font-family: "Lexend", sans-serif; font-weight: 600; font-size: 21px; line-height: 56px; color: var(--white); }

  /* Newsletter */
  .news-title { top: 1868px; font-family: "Lexend", sans-serif; font-weight: 500; font-size: 32px; color: var(--ink-soft); }
  .news-input { left: 340px; top: 1944px; width: 430px; height: 40px; border-bottom: 2px solid #9a9a9a; font-size: 14px; color: #9a9a9a; padding: 14px 0 0 8px; }
  .news-btn { left: 770px; top: 1942px; width: 132px; height: 42px; background: var(--accent); color: var(--white); font-family: "Lexend", sans-serif; font-weight: 600; font-size: 24px; text-align: center; line-height: 42px; }

  /* Footer */
  .site-footer { position: absolute; left: 0; top: 2084px; width: 1200px; height: 316px; background: var(--footer-bg); color: var(--white); }
  .footer-brand { left: 30px; width: 260px; top: 44px; text-align: center; font-size: 27px; white-space: nowrap; }
  .footer-tagline { left: 30px; width: 260px; text-align: center; font-family: "Lexend", sans-serif; font-weight: 600; font-size: 16px; }
  .footer-heading { top: 38px; font-family: "Lexend", sans-serif; font-weight: 500; font-size: 33px; }
  .footer-link { left: 546px; font-family: "Lexend", sans-serif; font-weight: 600; font-size: 16px; }
  .footer-field { left: 890px; width: 298px; background: var(--field-bg); font-size: 12px; color: #eeeeee; padding: 8px 0 0 6px; }
  .footer-send { left: 978px; top: 2308px; width: 76px; height: 30px; background: var(--white); color: var(--ink); border-radius: 15px; font-family: "Lexend", sans-serif; font-weight: 600; font-size: 16px; text-align: center; line-height: 30px; }
  .footer-rule { left: 0; top: 2358px; width: 1200px; height: 2px; background: #bbbbbb; }
  .copyright { top: 2372px; font-family: "Lexend", sans-serif; font-weight: 600; font-size: 15px; color: #cfcfcf; }
</style>
</head>
<body>

<header class="site-header">
  <div class="abs brand">ClaimVouchly.com</div>
  <nav class="abs main-nav">
    <a class="active">HOME</a>
    <a>CONTACT US</a>
    <a>TESTIMONIAL</a>
    <a>TERMS</a>
  </nav>
</header>

<svg class="hero-photo" role="img" aria-label="Desk scene photo: hand on a keyboard, mouse, yellow wristwatch and phone on a white desk" viewBox="0 0 1200 778">
  <defs>
    <radialGradient id="heroGlow" cx="50%" cy="45%" r="75%">
      <stop offset="0%" stop-color="var(--hero-light)"/>
      <stop offset="100%" stop-color="var(--hero-mid)"/>
    </radialGradient>
  </defs>
  <rect width="1200" height="778" fill="url(#heroGlow)"/>
</svg>

<h1 class="abs center-x hero-title">WELCOME TO THE REDEMPTION SOURCE</h1>
<p class="abs center-x hero-sub">PLEASE ENTER A VALID CERTIFICATE ID IN THE FORM BELOW</p>
<p class="abs center-x hero-note">TO REDEEM YOUR CERTIFICATE AND TO VIEW FAQ'S, TERMS AND LOCATIONS.</p>

<form class="abs redeem-form">
  <div class="redeem-input">ENTER...</div>
  <div class="redeem-btn">GO</div>
</form>

<section class="about">
  <p class="abs center-x about-line" style="top:946px">CLAIMVOUCHLY.COM IS A LEADING COMPANY IN TRAVEL CERTIFICATE FULFILLMENT.</p>
  <p class="abs center-x about-line" style="top:1012px">OUR GOAL IS TO MAKE IT EASY FOR YOU TO REDEEM YOUR CERTIFICATE AND OUR PHILOSOPHY IS THIS: "WHAT GOOD IS IT TO RECEIVE A</p>
  <p class="abs center-x about-line" style="top:1044px">GIFT CERTIFICATE IF YOU CAN'T USE IT?".</p>
  <p class="abs center-x about-line" style="top:1110px">IF YOU HAVE ANY QUESTIONS ABOUT HOW TO REDEEM A CERTAIN CERTIFICATE, PLEASE CONTACT US. WE ARE HERE TO HELP.</p>
</section>

<section class="testimonial">
  <svg class="testimonial-photo" role="img" aria-label="Dimmed desk photo: hand on a keyboard beside a notebook and phone" viewBox="0 0 1124 620">
    <defs>
      <linearGradient id="testiShade" x1="0" y1="0" x2="1" y2="1">
        <stop offset="0%" stop-color="var(--testi-mid)"/>
        <stop offset="100%" stop-color="var(--testi-dark)"/>
      </linearGradient>
    </defs>
    <rect width="1124" height="620" fill="url(#testiShade)"/>
  </svg>
  <h2 class="abs center-x testi-title">TESTIMONIAL</h2>
  <div class="abs testi-rule"></div>
  <svg class="abs" style="left:542px;top:1320px" width="116" height="116" viewBox="0 0 116 116" role="img" aria-label="Customer avatar">
    <circle cx="58" cy="58" r="58" fill="var(--white)"/>
    <circle cx="58" cy="58" r="40" fill="#d9b48f"/>
  </svg>
  <p class="abs center-x testi-name">MAYA R.</p>
  <p class="abs center-x testi-meta" style="top:1484px">SALEM, OR</p>
  <p class="abs center-x testi-meta" style="top:1502px">ADDED ON 06/23/2017 06:24:16 PM</p>
  <blockquote class="abs testi-quote">"HAZEL WAS A "SAVING GRACE." SHE FOLLOWED UP AND HELPED ME BOOK THE VACATION<br>AND AIR FARE. HAZEL WAS POSITIVE AND DID EVERYTHING SHE PROMISED TO DO. "</blockquote>
  <svg class="abs" style="left:540px;top:1690px" width="120" height="44" viewBox="0 0 120 44" aria-label="Previous and next">
    <circle cx="22" cy="22" r="19" fill="none" stroke="var(--white)" stroke-width="2"/>
    <polyline points="26,13 17,22 26,31" fill="none" stroke="var(--white)" stroke-width="2"/>
    <circle cx="98" cy="22" r="19" fill="none" stroke="var(--white)" stroke-width="2"/>
    <polyline points="94,13 103,22 94,31" fill="none" stroke="var(--white)" stroke-width="2"/>
  </svg>
</section>

<section class="newsletter">
  <h2 class="abs center-x news-title">GET OUR NEWSLATTER</h2>
  <div class="abs news-input">EMAIL...</div>
  <div class="abs news-btn">SEND</div>
</section>

<footer class="site-footer">
  <div class="abs footer-brand">ClaimVouchly.com</div>
  <p class="abs footer-tagline" style="top:116px">LOREM IPSUM DOLOR SIT</p>
  <p class="abs footer-tagline" style="top:140px">AMET, CONSECTETUR</p>

  <h3 class="abs footer-heading" style="left:546px">LINKS:</h3>
  <p class="abs footer-link" style="top:98px">HOME</p>
  <p class="abs footer-link" style="top:138px">CONTACT US</p>
  <p class="abs footer-link" style="top:180px">TESTIMONIAL</p>
  <p class="abs footer-link" style="top:220px">TERMS</p>

  <h3 class="abs footer-heading" style="left:894px">GET IN TOUCH:</h3>
</footer>
<div class="abs footer-field" style="top:2178px;height:38px">EMAIL...</div>
<div class="abs footer-field" style="top:2230px;height:62px">MESSEGE...</div>
<div class="abs footer-send">SEND</div>
<div class="abs footer-rule"></div>
<p class="abs center-x copyright">COP[YRIGHT ALL RIGHT RESERVES 7-17</p>

</body>
</html>
```